Crestwell Grand Piano Academy is a comprehensive piano studio located in CBD area and provide individual piano lessons.

We also provide services for wedding organising band, or instrumental hiring or venue hiring, or organise concert to students.

I want my name card to be very creative, does not have to be the form or shape with the normal name card, can be in different shape. Also, I want the name card to be very upper class, because learning piano is a serious thing, so I do not want people to bargain with the prices. I want people to see it as a very elegant tuition so that they do not want to bargain and think it is worth to try.

Further more, Crestwell Grand Piano Academy is not like normal piano studio only provide piano lessons, we provide band services for each other event, such as cruise party, wedding etc. I want people to see it as owner of Grand Piano Academy, they will have different type of services all in one, I provide more than that, and I am well connected. I do not provide only piano lesson, but also all other musical knowledge and I am very professional

I want name card to be very simple, just name of company name, my name and website that's all, maybe phone number and email as well.

Please check my website to have more ideal concept.
http://dorvanpeq.sitebuild.example/crestwellpianoacademy

Target Market(s)

For all people who love to play piano (better with upper class)

Industry/Entity Type

Wedding

Contact Information for Business Card

Clara Voss
Mobile:0419876502
Email: crestwellgrandstudio@mailbrook.example

Colors

Designer to choose colors to be used in the design.

Requirements
Must have
• Creativity
Nice to have
• Black and white
some sort of piano image
Should not have
• Childish

```html
<!DOCTYPE html>
<html lang="en">
<head>
<meta charset="utf-8">
<title>Crestwell Grand Piano Academy – Name Card</title>
<link href="https://fonts.googleapis.com/css2?family=Lobster+Two:ital,wght@1,700&family=Kalam:wght@400&display=swap" rel="stylesheet">
<style>
  :root {
    --canvas-bg: #f3f1ee;
    --card-bg: #ffffff;
    --ink: #111111;
    --rule: #1a1a1a;
    --ornament-tone: #cfcfcf;
    --illustration-tone: #d9d9d9;
  }
  * { box-sizing: border-box; margin: 0; padding: 0; }
  html, body {
    width: 1200px;
    height: 900px;
    overflow: hidden;
    background: var(--canvas-bg);
  }
  .canvas {
    position: relative;
    width: 1200px;
    height: 900px;
  }
  .card {
    position: absolute;
    background: var(--card-bg);
    border: 5px solid var(--ink);
    box-shadow: 0 10px 24px rgba(0,0,0,0.18);
  }

  /* Front of card */
  .card-front {
    left: 90px;
    top: 90px;
    width: 580px;
    height: 320px;
  }
  .front-frame {
    position: absolute;
    left: 50px;
    right: 50px;
    top: 100px;
    height: 110px;
  }
  .front-rule {
    position: absolute;
    left: 0;
    right: 0;
    height: 2px;
    background: var(--rule);
    border-radius: 50%;
  }
  .front-rule.top { top: 14px; }
  .front-rule.bottom { bottom: 14px; }
  .ornament {
    position: absolute;
    left: 50%;
    width: 60px;
    height: 26px;
    margin-left: -30px;
    background: var(--ornament-tone);
    border-radius: 6px;
  }
  .ornament.top { top: 2px; }
  .ornament.bottom { bottom: 2px; }
  .academy-title {
    position: absolute;
    left: 0;
    right: 0;
    top: 36px;
    text-align: center;
    font-family: "Lobster Two", cursive;
    font-style: italic;
    font-weight: 700;
    font-size: 30px;
    color: var(--ink);
    letter-spacing: 0.5px;
  }

  /* Back of card */
  .card-back {
    left: 500px;
    top: 470px;
    width: 600px;
    height: 330px;
  }
  .contact-block {
    position: absolute;
    right: 200px;
    top: 115px;
    text-align: right;
    color: var(--ink);
  }
  .owner-name {
    font-family: "Lobster Two", cursive;
    font-style: italic;
    font-weight: 700;
    font-size: 30px;
    line-height: 36px;
    margin-bottom: 8px;
  }
  .contact-line {
    font-family: "Kalam", cursive;
    font-size: 12px;
    line-height: 17px;
    white-space: nowrap;
    padding-right: 24px;
  }
  .piano-illustration {
    position: absolute;
    right: 35px;
    top: 105px;
    width: 150px;
    height: 140px;
    background: linear-gradient(160deg, var(--illustration-tone), #f2f2f2);
    border-radius: 4px;
  }
</style>
</head>
<body>
<main class="canvas">
  <section class="card card-front" aria-label="Card front">
    <div class="front-frame">
      <div class="ornament top" role="img" aria-label="Small scroll ornament"></div>
      <div class="front-rule top"></div>
      <h1 class="academy-title">Crestwell Grand Piano Academy</h1>
      <div class="front-rule bottom"></div>
      <div class="ornament bottom" role="img" aria-label="Small scroll ornament"></div>
    </div>
  </section>

  <section class="card card-back" aria-label="Card back">
    <div class="contact-block">
      <p class="owner-name">Clara Voss</p>
      <p class="contact-line">mob :0419 876 502</p>
      <p class="contact-line">email: crestwellgrandstudio@mailbrook.example</p>
      <p class="contact-line">http://dorvanpeq.sitebuild.example/crestwellpianoacademy</p>
    </div>
    <div class="piano-illustration" role="img" aria-label="Line drawing of a grand piano with open lid and keyboard"></div>
  </section>
</main>
</body>
</html>
```